We operate a niche online Job Board in Australia. The website is called 'Harvest Roles Australia' and is used by Christian Employers to advertise their job vacancies.
I would like a business card that identifies with our website (www.harvestroles-example.com.au). We would like the same colors and fonts used on our business card from our website. When people look at our business card we want them to be able to recognise it from the website.
We want the web address to be dominant.
Updates
We are liking those that use white space as well as the blue and orange and those that highlight the url.
We now have 60 designs and therefore will not wait for the Sunday deadline to make a decision. We have a few we like.
The ones we like are:
- bold
- creative
- colorful (blue orange and white)
- some white space
- no boxes or borders
- font the same as our website
- reflects the look of our website
We will make a final decision in the next 6 hours so please if you think you have something to offer then get it in within the next 6 hours. If you think you will leave it till later you will miss out. Thanks to all those who have responded with some great designs, sorry we can't reward all of you!
Industry/Entity Type
Business
Contact Information for Business Card
Harvest Roles Australia
www.harvestroles-example.com.au
Peter Galvridge
CEO
Phone: 1300 512 874
Mobile: 0412 735019
Fax: (03) 9157 2360
email: peter@harvestroles-example.com.au
Requirements
Should not have
- We do not want a cross or any cliche christian images.

```html
<!DOCTYPE html>
<html lang="en">
<head>
<meta charset="utf-8">
<title>Harvest Roles Australia – Business Card</title>
<link rel="stylesheet" href="https://fonts.googleapis.com/css2?family=PT+Serif&family=Arimo:wght@400;700&family=Tinos&family=Noto+Sans:wght@600&display=swap">
<style>
  :root {
    --navy: #0b0f63;
    --orange: #f7931e;
    --white: #ffffff;
    --ink: #111111;
    --stage: #2b2b2b;
  }
  * { box-sizing: border-box; margin: 0; padding: 0; }
  html, body { width: 1200px; height: 942px; overflow: hidden; }
  body { background: var(--stage); position: relative; }

  .card {
    position: absolute;
    top: 328px;
    width: 500px;
    height: 286px;
    overflow: hidden;
  }

  /* Front */
  .card--front { left: 70px; background: var(--navy); }
  .front__name {
    position: absolute; left: 42px; top: 98px;
    font-family: "PT Serif", serif;
    font-size: 54px; color: var(--white); letter-spacing: -0.5px;
  }
  .front__band {
    position: absolute; left: 0; right: 0; top: 222px; height: 34px;
    background: var(--orange);
    display: flex; align-items: center; justify-content: flex-end;
    padding-right: 30px;
  }
  .front__url {
    font-family: "Noto Sans", sans-serif; font-weight: 600;
    font-size: 17px; letter-spacing: 1.6px; color: var(--white);
  }

  /* Back */
  .card--back { left: 630px; background: var(--white); }
  .back__header {
    position: absolute; left: 0; right: 0; top: 18px; height: 26px;
    background: var(--navy);
  }
  .back__brand {
    position: absolute; left: 22px; top: 18px;
    background: var(--navy);
    padding: 5px 10px 4px;
    border-right: 3px solid var(--white);
    font-family: "Tinos", serif; color: var(--white); line-height: 1;
  }
  .back__brand-name { font-size: 19px; display: block; }
  .back__brand-region { font-size: 9px; display: block; text-align: right; margin-top: 2px; }
  .back__url {
    position: absolute; right: 18px; top: 22px;
    font-family: "Arimo", sans-serif; font-weight: 700;
    font-size: 15px; color: var(--white);
  }
  .back__person {
    position: absolute; left: 50px; top: 88px;
    font-family: "Arimo", sans-serif; font-size: 29px; color: var(--ink);
  }
  .back__contacts {
    position: absolute; left: 60px; top: 140px;
    list-style: none;
    font-family: "Tinos", serif; font-size: 16px; color: var(--ink);
  }
  .back__contacts li { display: flex; align-items: center; gap: 8px; margin-bottom: 10px; }
  .back__contacts li:nth-child(2) { padding-left: 50px; }
  .back__contacts svg { flex: none; }
  .back__footer {
    position: absolute; left: 0; right: 0; top: 228px; height: 26px;
    background: var(--orange);
    display: flex; align-items: center; justify-content: space-between;
    padding: 0 24px;
    font-family: "Tinos", serif; font-size: 16px; color: var(--ink);
  }
  .back__label { color: var(--navy); font-family: "Arimo", sans-serif; font-weight: 700; font-size: 14px; }
</style>
</head>
<body>

  <section class="card card--front" aria-label="Business card front">
    <div class="front__name">Harvest Roles</div>
    <div class="front__band">
      <span class="front__url">www.harvestroles-example.com.au</span>
    </div>
  </section>

  <section class="card card--back" aria-label="Business card back">
    <div class="back__header"></div>
    <div class="back__brand">
      <span class="back__brand-name">Harvest Roles</span>
      <span class="back__brand-region">Australia</span>
    </div>
    <div class="back__url">www.harvestroles-example.com.au</div>

    <h1 class="back__person">Peter Galvridge CEO</h1>

    <ul class="back__contacts">
      <li>
        <svg width="20" height="15" viewBox="0 0 20 15" aria-hidden="true">
          <rect x="1" y="1" width="18" height="13" fill="none" stroke="#0b0f63" stroke-width="1.6"/>
          <path d="M1 1 L10 8 L19 1" fill="none" stroke="#0b0f63" stroke-width="1.6"/>
        </svg>
        peter@harvestroles-example.com.au
      </li>
      <li>
        <svg width="12" height="20" viewBox="0 0 12 20" aria-hidden="true">
          <rect x="1" y="1" width="10" height="18" rx="2" fill="none" stroke="#0b0f63" stroke-width="1.5"/>
          <line x1="3" y1="4" x2="9" y2="4" stroke="#0b0f63"/>
          <circle cx="6" cy="16" r="1.2" fill="#0b0f63"/>
        </svg>
        0412 735019
      </li>
    </ul>

    <div class="back__footer">
      <span><span class="back__label">Phone:</span> 1300 512 874</span>
      <span><span class="back__label">Fax:</span> (03) 9157 2360</span>
    </div>
  </section>

</body>
</html>
```